New Business Card Design Project

Updated business card design. I am moving towards more coaching of, for the most part women, who are searching for more in their lives. I am an intuitive healer, homeopath and nutritionist but also an author and motivational speaker. Int the past I have included my photo on the card but that is not essential. My book is called the Brilliance of Saffron - Reclaiming the Shade of Your Spirit so my colours are typically magenta.
Target Market(s)
Women - 35 - 60 considering improving their health. However, I am also a professional speaker with a target audience including corporate and conferences.
Industry/Entity Type
Health And Wellness
Contact Information for Business Card
Delia Tranmoor, Hom, RHN, BA
www.deliatranmoor.example
delia@deliatranmoor.example
555-203-7914
Facebook, instagram and twitter logos
Look and feel
Each slider illustrates characteristics of the customer's brand and the style your logo design should communicate.

```html
<!DOCTYPE html>
<html lang="en">
<head>
<meta charset="utf-8">
<title>Delia Tranmoor – Business Card</title>
<link href="https://fonts.googleapis.com/css2?family=Lato:wght@400;700&display=swap" rel="stylesheet">
<style>
  :root {
    --magenta: #e8277a;
    --ink: #1f1f1f;
    --card: #fbfbfb;
    --backdrop: #ececec;
    --photo-light: #c9b49a;
    --photo-mid: #6f7d55;
    --photo-dark: #3e4a30;
  }
  html, body {
    margin: 0;
    width: 1200px;
    height: 961px;
    overflow: hidden;
    background: var(--backdrop);
    font-family: "Lato", sans-serif;
  }
  .business-card {
    position: absolute;
    left: 190px;
    top: 233px;
    width: 821px;
    height: 494px;
    background: var(--card);
    overflow: hidden;
    color: var(--ink);
  }
  .accent-bar {
    position: absolute;
    left: 58px;
    width: 5px;
    background: var(--magenta);
  }
  .accent-bar--top { top: 0; height: 262px; }
  .accent-bar--bottom { top: 450px; height: 44px; }
  .brand {
    position: absolute;
    left: 0;
    right: 0;
    top: 48px;
    display: flex;
    justify-content: center;
    align-items: center;
    gap: 14px;
  }
  .brand__dot {
    width: 30px;
    height: 30px;
    border-radius: 50%;
    background: var(--magenta);
  }
  .brand__name {
    font-size: 44px;
    font-weight: 400;
    color: var(--ink);
    letter-spacing: 0.5px;
  }
  .contact-block {
    position: absolute;
    left: 51px;
    top: 270px;
  }
  .contact-block__name {
    margin: 0;
    font-size: 21px;
    font-weight: 400;
    color: var(--magenta);
    letter-spacing: 0.3px;
  }
  .contact-block__credentials {
    margin: 4px 0 0;
    font-size: 16px;
  }
  .contact-list {
    list-style: none;
    margin: 26px 0 0;
    padding: 0;
    font-size: 16px;
  }
  .contact-list li {
    display: flex;
    align-items: center;
    gap: 12px;
    height: 30px;
  }
  .contact-list svg { width: 16px; height: 14px; fill: var(--magenta); }
  .contact-block__web {
    margin: 4px 0 0;
    font-size: 17px;
    font-weight: 700;
    color: var(--magenta);
    letter-spacing: 1.4px;
  }
  .portrait {
    position: absolute;
    left: 464px;
    top: 142px;
    width: 372px;
    height: 372px;
    border-radius: 50%;
    background: radial-gradient(circle at 65% 45%, var(--photo-light) 0%, var(--photo-mid) 55%, var(--photo-dark) 100%);
  }
</style>
</head>
<body>
  <div class="business-card">
    <div class="accent-bar accent-bar--top"></div>
    <div class="accent-bar accent-bar--bottom"></div>

    <div class="brand">
      <span class="brand__dot"></span>
      <span class="brand__name">Delia Tranmoor</span>
    </div>

    <div class="contact-block">
      <h1 class="contact-block__name">DELIA TRANMOOR</h1>
      <p class="contact-block__credentials">Hom, RHN, BA</p>
      <ul class="contact-list">
        <li>
          <svg viewBox="0 0 16 14" aria-hidden="true"><path d="M1 4 Q8 -1 15 4 L13 6 L11 4 L5 4 L3 6 Z M4 7 L12 7 L14 13 L2 13 Z"/></svg>
          <span>555-203-7914</span>
        </li>
        <li>
          <svg viewBox="0 0 16 14" aria-hidden="true"><path d="M1 2 H15 V12 H1 Z M2 3 L8 8 L14 3" stroke="#fbfbfb" stroke-width="1.2"/></svg>
          <span>delia@deliatranmoor.example</span>
        </li>
      </ul>
      <p class="contact-block__web">www.deliatranmoor.example</p>
    </div>

    <div class="portrait" role="img" aria-label="Portrait photo of Delia Tranmoor standing beside a brick wall with greenery"></div>
  </div>
</body>
</html>
```